Velmora Systems 4-Brochure Package

Design an overall look-n-feel (a template). Then implement for a family of 4 brochures:
1. Unified Communications
2. App & Mobile Development
3. Telemedicine
4. Managed Services

Will need to incorporate content, diagrams, and photographs into each of the brochures (all provided).

Photographs need to be "layered" and colorized to match the overall brand concept of intersecting circles where the middle is the "velmora" (and the Q resides). See Concepts provided. (Colors: Pantone Blue 072C, Pantone 279C- 80% Opacity, Process Cyan 80% Opacity)

Utilize image "Velmora Infrastructure Background" as the background (refer to look of website listed below).

New website is under development and can be viewed at: http://brindlestudio-example.com/velmora/

Target Market(s)

Chief Information Officers and IT Professionals, Industries include health, hospitals, technology, manufacturing, government.

Industry/Entity Type

Communications

Requirements
Must have
• Need to use the blue-colorized photos (raw images provided). Need to match branded color palette (noted above in brief) - Refer to Brand Comps provided also.

Include both addresses:

SACRAMENTO:
1730 Kestrel Ridge Way, Suite 410
Sacramento, CA 95840
916.555.0142
Toll-free: 1.866.555.0197

CHICO:
468 Larkspur Lane, Suite 220
Chico, CA 95931
530.555.0168
Toll-free: 1.866.555.0197

```html
<!DOCTYPE html>
<html lang="en">
<head>
<meta charset="utf-8">
<title>Velmora Systems — Unified Communications Brochure</title>
<link rel="stylesheet" href="https://fonts.googleapis.com/css2?family=Lato:wght@400;700;900&family=Archivo+Narrow:wght@400;600&display=swap">
<style>
  :root {
    --backdrop: #ecebe8;
    --brand-blue: #2f86dc;
    --brand-blue-deep: #1f6bc4;
    --brand-navy: #1212a0;
    --sky-pale: #b9d4f2;
    --sky-mid: #7fb0e6;
    --ink: #1d1d1d;
    --white: #ffffff;
    --logo-navy: #1c2f8c;
  }
  * { box-sizing: border-box; margin: 0; padding: 0; }
  html, body { width: 1200px; height: 900px; overflow: hidden; }
  body { background: var(--backdrop); position: relative; font-family: "Lato", sans-serif; }

  .brochure { position: absolute; left: 31px; top: 45px; width: 1140px; height: 807px; background: var(--white); overflow: hidden; }

  .hero-photo {
    position: absolute; left: 0; top: 0; width: 380px; height: 316px;
    background: linear-gradient(135deg, #1f5fae 0%, #4a8fd8 45%, #a9cdf2 100%);
  }
  .intro {
    position: absolute; left: 380px; top: 0; width: 380px; height: 316px;
    background: linear-gradient(180deg, var(--brand-blue) 0%, var(--brand-blue-deep) 100%);
    color: var(--white); padding: 21px 20px 0 27px;
  }
  .intro-headline { font-weight: 700; font-size: 19.5px; line-height: 21px; letter-spacing: .2px; width: 300px; margin-bottom: 17px; }
  .intro-body { font-size: 15px; line-height: 19px; width: 330px; }

  .contact {
    position: absolute; left: 760px; top: 0; width: 380px; height: 316px;
    background: var(--brand-navy); color: var(--white); padding: 75px 24px 0 24px;
    font-size: 15px; line-height: 19px;
  }
  .office + .office { margin-top: 19px; }
  .office-city { font-weight: 700; text-decoration: underline; }

  .diagram-panel {
    position: absolute; left: 0; top: 316px; width: 760px; height: 491px;
    background:
      linear-gradient(90deg, #ffffff 0%, #ededed 100%) 0 0 / 380px 100% no-repeat,
      linear-gradient(90deg, #ffffff 0%, #ecf3fc 45%, var(--sky-pale) 100%) 380px 0 / 380px 100% no-repeat;
  }
  .diagram { position: absolute; left: 0; top: 0; width: 760px; height: 491px; }
  .node-label { font-family: "Lato", sans-serif; font-weight: 700; font-size: 11px; fill: var(--white); }
  .feature-list { font-family: "Archivo Narrow", sans-serif; font-size: 10.5px; fill: var(--ink); }

  .infrastructure {
    position: absolute; left: 760px; top: 316px; width: 380px; height: 391px;
    background: linear-gradient(180deg, var(--sky-mid) 0%, #9cc2ec 50%, var(--sky-pale) 100%);
  }
  .signoff {
    position: absolute; left: 760px; top: 707px; width: 380px; height: 100px;
    background: linear-gradient(180deg, #d2d2d2 0%, #f4f4f4 100%);
  }
  .wordmark { position: absolute; right: 24px; top: 34px; display: flex; align-items: center; gap: 10px; }
  .wordmark-dot { width: 30px; height: 30px; border-radius: 50%; background: var(--brand-blue); }
  .wordmark-name { font-family: "Lato", sans-serif; font-weight: 700; font-size: 19px; color: var(--logo-navy); }
</style>
</head>
<body>
<main class="brochure">
  <div class="hero-photo" role="img" aria-label="Blue-tinted photo of a professional at a desktop monitor on a video call"></div>

  <section class="intro">
    <h1 class="intro-headline">Velmora Systems delivers success by unifying all communications into a single, seamless and cohesive Unified Communications and Collaboration platform.</h1>
    <p class="intro-body">Velmora’s Unified Communications solution is delivered over the cloud using standard internet connections thereby eliminating costly analog lines and on-premise hardware and software. With no hardware to deploy and maintain, there’s no obsolescence to worry about.</p>
  </section>

  <section class="contact">
    <div class="office">
      <div class="office-city">SACRAMENTO:</div>
      <div>1730 Kestrel Ridge Way, Suite 410</div>
      <div>Sacramento, CA 95840</div>
      <div>916.555.0142</div>
      <div>Toll-free: 1.866.555.0197</div>
    </div>
    <div class="office">
      <div class="office-city">CHICO:</div>
      <div>468 Larkspur Lane, Suite 220</div>
      <div>Chico, CA 95931</div>
      <div>530.555.0168</div>
      <div>Toll-free: 1.866.555.0197</div>
    </div>
  </section>

  <section class="diagram-panel">
    <svg class="diagram" viewBox="31 361 760 491" xmlns="http://www.w3.org/2000/svg">
      <defs>
        <radialGradient id="node-fill" cx="50%" cy="30%" r="75%">
          <stop offset="0" stop-color="#6f90c8"/>
          <stop offset=".6" stop-color="#3d63a6"/>
          <stop offset="1" stop-color="#213f7c"/>
        </radialGradient>
        <linearGradient id="arrow-fill" x1="0" y1="0" x2="0" y2="1">
          <stop offset="0" stop-color="#6f90c8"/>
          <stop offset="1" stop-color="#2b4a8a"/>
        </linearGradient>
        <radialGradient id="thumb-fill" cx="40%" cy="35%" r="70%">
          <stop offset="0" stop-color="#f2f2f2"/>
          <stop offset=".6" stop-color="#b9bcc2"/>
          <stop offset="1" stop-color="#5d6470"/>
        </radialGradient>
        <polygon id="flow-arrow" points="-14,-8 2,-8 2,-15 16,0 2,15 2,8 -14,8" fill="url(#arrow-fill)" stroke="#ffffff" stroke-width="1"/>
      </defs>

      <use href="#flow-arrow" transform="translate(338 520) rotate(-35)"/>
      <use href="#flow-arrow" transform="translate(487 518) rotate(35)"/>
      <use href="#flow-arrow" transform="translate(537 656) rotate(90)"/>
      <use href="#flow-arrow" transform="translate(413 742) rotate(180)"/>
      <use href="#flow-arrow" transform="translate(300 662) rotate(-90)"/>

      <g class="node">
        <circle cx="415" cy="468" r="61" fill="url(#node-fill)" stroke="#1d3a74" stroke-width="1.5"/>
        <text class="node-label" x="415" y="467" text-anchor="middle">Business Voice</text>
        <text class="node-label" x="415" y="481" text-anchor="middle">Services</text>
      </g>
      <g class="node">
        <circle cx="557" cy="576" r="60" fill="url(#node-fill)" stroke="#1d3a74" stroke-width="1.5"/>
        <text class="node-label" x="557" y="572" text-anchor="middle">Call Center</text>
        <text class="node-label" x="557" y="586" text-anchor="middle">Services</text>
      </g>
      <g class="node">
        <circle cx="503" cy="743" r="60" fill="url(#node-fill)" stroke="#1d3a74" stroke-width="1.5"/>
        <text class="node-label" x="503" y="741" text-anchor="middle">Interoperability</text>
        <text class="node-label" x="503" y="755" text-anchor="middle">Features</text>
      </g>
      <g class="node">
        <circle cx="324" cy="743" r="60" fill="url(#node-fill)" stroke="#1d3a74" stroke-width="1.5"/>
        <text class="node-label" x="324" y="741" text-anchor="middle">Messaging</text>
        <text class="node-label" x="324" y="755" text-anchor="middle">Services</text>
      </g>
      <g class="node">
        <circle cx="265" cy="576" r="60" fill="url(#node-fill)" stroke="#1d3a74" stroke-width="1.5"/>
        <text class="node-label" x="265" y="572" text-anchor="middle">Collaboration</text>
        <text class="node-label" x="265" y="586" text-anchor="middle">Services</text>
      </g>
      <g class="node">
        <circle cx="401" cy="630" r="60" fill="url(#node-fill)" stroke="#1d3a74" stroke-width="1.5"/>
        <text class="node-label" x="401" y="628" text-anchor="middle">Unifying</text>
        <text class="node-label" x="401" y="642" text-anchor="middle">Features</text>
      </g>

      <circle cx="457" cy="416" r="33" fill="url(#thumb-fill)" role="img" aria-label="Small photo of a connected network node graphic"/>
      <circle cx="592" cy="529" r="33" fill="url(#thumb-fill)" role="img" aria-label="Small photo of a call center agent with a headset"/>
      <circle cx="454" cy="592" r="31" fill="url(#thumb-fill)" role="img" aria-label="Small photo of interlocking puzzle pieces"/>
      <circle cx="549" cy="781" r="31" fill="url(#thumb-fill)" role="img" aria-label="Small photo of two colleagues wearing headsets"/>
      <circle cx="258" cy="762" r="33" fill="url(#thumb-fill)" role="img" aria-label="Small photo of a hand holding a mobile phone"/>
      <circle cx="211" cy="530" r="33" fill="url(#thumb-fill)" role="img" aria-label="Small photo of people working at a laptop"/>

      <text class="feature-list">
        <tspan x="510" y="419">•  Unlimited Virtual PBX</tspan>
        <tspan x="510" y="433">•  Intelligent Call Routing</tspan>
        <tspan x="510" y="447">•  Personal Conferencing</tspan>
        <tspan x="510" y="461">•  Call Recording</tspan>
        <tspan x="510" y="475">•  RoamCall</tspan>
      </text>
      <text class="feature-list">
        <tspan x="602" y="622">•  Unlimited Virtual Call Center</tspan>
        <tspan x="602" y="636">•  Supervisory Modes</tspan>
        <tspan x="602" y="650">•  Live-Monitor</tspan>
        <tspan x="602" y="664">•  Call Recording</tspan>
      </text>
      <text class="feature-list">
        <tspan x="389" y="668">•  Unified Command Center</tspan>
        <tspan x="389" y="682">•  Real-Time Presence</tspan>
        <tspan x="389" y="696">•  Administration</tspan>
        <tspan x="389" y="710">•  Multi-Location</tspan>
      </text>
      <text class="feature-list">
        <tspan x="579" y="714">•  CloudLedger Call Adapter</tspan>
        <tspan x="579" y="728">•  MailDesk Integration</tspan>
        <tspan x="579" y="742">•  Analog Phone Support</tspan>
        <tspan x="579" y="756">•  NetLinkPlus</tspan>
      </text>
      <text class="feature-list">
        <tspan x="119" y="714">•  Full Featured Hosted Email</tspan>
        <tspan x="119" y="728">•  Secure IM/Text Messaging</tspan>
        <tspan x="119" y="742">•  Personal Fax to Email</tspan>
        <tspan x="119" y="756">•  RoamMessage</tspan>
      </text>
      <text class="feature-list">
        <tspan x="100" y="622">•  Full Featured Web Meeting</tspan>
        <tspan x="100" y="636">•  1 Click Desktop Sharing</tspan>
        <tspan x="100" y="650">•  Remote Desktop Access</tspan>
      </text>
    </svg>
  </section>

  <div class="infrastructure" role="img" aria-label="Pale blue-tinted photo of data center server racks"></div>

  <footer class="signoff">
    <div class="wordmark">
      <span class="wordmark-dot"></span>
      <span class="wordmark-name">Velmora Systems</span>
    </div>
  </footer>
</main>
</body>
</html>
```